harvest Soon Book Cover Design for real estate investment book

I am looking for a Book Cover design for my new book. I would like designs for a hardcover, softcover and Lumora book.

The book deals with real estate and mortgage investments. Looking for a clean, bright simple design. Want to cover to be White with big RED letters. See "Dancing past Noon" book for an example ... see attached.

Target Market(s)

Affluent people with money looking for investment solutions.

Industry/Entity Type

Financial Service

Font styles to use
Serif

Requirements
Must have
• Bright clean design that will be appealing to affluent people.
• Title: harvest SOON
• Subtitle: A quiet method for thriving through land holdings
• subsubtitle: Secrets the Bank Teller Keeps Hidden From Clients...
• Author: Ned Falconby
• My Picture on the inside cover or on the back cover
• Book Description, Author description
Nice to have
• Focus on the Front cover look and feel first. Then we can look at the inside flaps and back cover. I will need to send you text. This is for the full cover. Front. Back. Spine. Inside flaps fro hardcover.

```html
<!DOCTYPE html>
<html lang="en">
<head>
<meta charset="utf-8">
<title>harvest SOON — Ned Falconby</title>
<link rel="stylesheet" href="https://fonts.googleapis.com/css2?family=Archivo+Black&family=Arimo:wght@700&family=Montserrat:wght@700&family=Roboto+Condensed:wght@400;500&display=swap">
<style>
  :root {
    --page: #ffffff;
    --ink: #111111;
    --red: #e00000;
    --band: #1c1c1c;
    --band-text: #ffffff;
    --sky: #9db3c8;
    --lawn: #b9cf8f;
  }
  html, body {
    margin: 0;
    width: 1200px;
    height: 1200px;
    overflow: hidden;
    background: var(--page);
  }
  .cover-canvas { display: block; width: 1200px; height: 1200px; }
  .kicker { font-family: "Roboto Condensed", "Arial Narrow", sans-serif; font-weight: 400; fill: var(--ink); }
  .kicker-accent { fill: var(--red); font-weight: 500; }
  .title-top { font-family: "Arimo", Arial, sans-serif; font-weight: 700; fill: var(--ink); }
  .title-bottom { font-family: "Archivo Black", "Arial Black", sans-serif; fill: var(--red); }
  .title-bang { fill: var(--red); }
  .subtitle { font-family: "Roboto Condensed", "Arial Narrow", sans-serif; font-weight: 400; fill: var(--ink); }
  .author-band { fill: var(--band); }
  .author-name { font-family: "Montserrat", Arial, sans-serif; font-weight: 700; fill: var(--band-text); letter-spacing: 4px; }
</style>
</head>
<body>
<svg class="cover-canvas" viewBox="0 0 1200 1200" xmlns="http://www.w3.org/2000/svg">
  <defs>
    <linearGradient id="sceneFill" x1="0" y1="0" x2="0" y2="1">
      <stop offset="0" stop-color="#8fa9c2"/>
      <stop offset="0.32" stop-color="#c9d6e2"/>
      <stop offset="0.45" stop-color="#9fba84"/>
      <stop offset="0.62" stop-color="#c7dba3"/>
      <stop offset="1" stop-color="#ffffff"/>
    </linearGradient>
    <radialGradient id="paperShade" cx="0.5" cy="0.55" r="0.75">
      <stop offset="0.6" stop-color="#ffffff"/>
      <stop offset="1" stop-color="#dcdcdc"/>
    </radialGradient>
  </defs>

  <!-- cover body -->
  <rect class="cover" x="231" y="19" width="775" height="1162" fill="url(#paperShade)"/>

  <!-- photo area -->
  <rect class="cover-photo" x="231" y="19" width="775" height="545" fill="url(#sceneFill)"
        role="img" aria-label="Photo of a red For Sale sign on a white post in front of a white suburban house with a green lawn under a cloudy blue sky"/>

  <!-- kicker line -->
  <text class="kicker" x="304" y="591" font-size="25" textLength="655" lengthAdjust="spacingAndGlyphs">Secrets the Bank Teller Keeps <tspan class="kicker-accent" font-size="35">Hidden</tspan> From Clients...</text>

  <!-- title -->
  <text class="title-top" x="288" y="765" font-size="168" textLength="590" lengthAdjust="spacingAndGlyphs">harvest</text>
  <text class="title-bottom" x="286" y="919" font-size="166" textLength="592" lengthAdjust="spacingAndGlyphs">SOON</text>
  <g class="title-bang" aria-hidden="true">
    <polygon points="896,650 962,650 946,858 912,858"/>
    <rect x="905" y="870" width="50" height="49"/>
  </g>

  <!-- subtitle -->
  <text class="subtitle" x="290" y="988" font-size="30" textLength="656" lengthAdjust="spacingAndGlyphs">A quiet method for thriving through land holdings</text>

  <!-- author band -->
  <rect class="author-band" x="231" y="1062" width="775" height="119"/>
  <text class="author-name" x="618" y="1138" font-size="46" text-anchor="middle">NED FALCONBY</text>
</svg>
</body>
</html>
```